Minimalist Modern Business Card Design, open to ideas, or cleaner version of provided files, but what logo & logo colors (with some black) as shown in files, and info for back shown in files as well.

```html
<!DOCTYPE html>
<html lang="en">
<head>
<meta charset="utf-8">
<title>Quillmere Fleet Care – Business Card</title>
<link rel="stylesheet" href="https://fonts.googleapis.com/css2?family=Montserrat:wght@400;500;600;700&display=swap">
<style>
  :root {
    --navy: #25266a;
    --ink: #1b1b1f;
    --paper: #ffffff;
    --backdrop: #b3b3b3;
  }
  * { box-sizing: border-box; margin: 0; padding: 0; }
  html, body { width: 1200px; height: 900px; overflow: hidden; }
  body {
    background: var(--backdrop);
    font-family: "Montserrat", sans-serif;
    position: relative;
  }
  .card {
    position: absolute;
    left: 250px;
    width: 700px;
    height: 400px;
    border-radius: 18px;
    overflow: hidden;
  }
  .card--front { top: 35px; background: var(--paper); }
  .card--back { top: 465px; background: var(--navy); }

  .brand {
    display: flex;
    align-items: center;
    gap: 16px;
    font-weight: 600;
    letter-spacing: 0.5px;
    white-space: nowrap;
  }
  .brand__square { width: 26px; height: 26px; flex: none; }
  .brand--front { position: absolute; left: 64px; top: 70px; font-size: 38px; color: var(--navy); }
  .brand--front .brand__square { background: var(--navy); }
  .brand--back {
    position: absolute; inset: 0;
    justify-content: center;
    font-size: 44px; color: var(--paper);
  }
  .brand--back .brand__square { background: var(--paper); width: 30px; height: 30px; }

  .person {
    position: absolute;
    left: 64px; top: 200px;
    width: 240px;
    text-align: right;
  }
  .person__name { font-size: 26px; font-weight: 700; color: var(--navy); }
  .person__title { font-size: 15px; font-weight: 500; color: var(--ink); margin-top: 4px; }

  .divider {
    position: absolute;
    left: 330px; top: 190px;
    width: 2px; height: 110px;
    background: var(--navy);
  }

  .contacts {
    position: absolute;
    left: 356px; top: 196px;
    list-style: none;
    display: flex; flex-direction: column; gap: 14px;
  }
  .contacts__item {
    display: flex; align-items: center; gap: 12px;
    font-size: 15px; color: var(--ink);
    white-space: nowrap;
  }
  .contacts__icon { width: 18px; height: 18px; flex: none; }

  .address-band {
    position: absolute;
    left: 0; right: 0; bottom: 0;
    height: 58px;
    background: var(--navy);
    color: var(--paper);
    font-size: 16px;
    font-weight: 500;
    display: flex; align-items: center; justify-content: center;
    letter-spacing: 0.3px;
  }
</style>
</head>
<body>

<section class="card card--front">
  <div class="brand brand--front">
    <span class="brand__square"></span>
    <span class="brand__name">Quillmere Fleet Care</span>
  </div>

  <div class="person">
    <p class="person__name">Daniel Carver</p>
    <p class="person__title">President</p>
  </div>

  <div class="divider"></div>

  <ul class="contacts">
    <li class="contacts__item">
      <svg class="contacts__icon" viewBox="0 0 24 24" aria-hidden="true">
        <path fill="#25266a" d="M6.6 10.8a15.1 15.1 0 0 0 6.6 6.6l2.2-2.2a1 1 0 0 1 1-.25 11.4 11.4 0 0 0 3.6.57 1 1 0 0 1 1 1V20a1 1 0 0 1-1 1A17 17 0 0 1 3 4a1 1 0 0 1 1-1h3.5a1 1 0 0 1 1 1c0 1.25.2 2.45.57 3.57a1 1 0 0 1-.25 1z"/>
      </svg>
      <span>555-014-2290</span>
    </li>
    <li class="contacts__item">
      <svg class="contacts__icon" viewBox="0 0 24 24" aria-hidden="true">
        <rect x="2" y="5" width="20" height="14" rx="2" fill="#25266a"/>
        <path d="M3 6.5l9 6.5 9-6.5" fill="none" stroke="#fff" stroke-width="1.6"/>
      </svg>
      <span>hello@quillmerefleet.com</span>
    </li>
    <li class="contacts__item">
      <svg class="contacts__icon" viewBox="0 0 24 24" aria-hidden="true">
        <circle cx="12" cy="12" r="10" fill="#25266a"/>
        <path d="M2 12h20M12 2c3 3 3 17 0 20M12 2c-3 3-3 17 0 20" fill="none" stroke="#fff" stroke-width="1.3"/>
      </svg>
      <span>www.quillmerefleet.com</span>
    </li>
  </ul>

  <div class="address-band">418 Harbor Ridge Ave Suite 20 Portland OR 97205</div>
</section>

<section class="card card--back">
  <div class="brand brand--back">
    <span class="brand__square"></span>
    <span class="brand__name">Quillmere Fleet Care</span>
  </div>
</section>

</body>
</html>
```